Vesk Architecture

We are a architectural design and build company working between scales 1/1000 to 1/1 we want people to understand our difference from our design experience and quality.we build hotels restourants and office spaces.Our company name is Vesk architecture to mind sustainability.

We want to write our adress phone and work spesifications on the card and we want our logo as backround.

Ps:you could find the logo adress and phone box numbers from the web:www.veskmimarlik-ornek.com

Target Market(s)

Who looks for experts.

Industry/Entity Type

Architecture

Requirements
Must have
• Design is over everything.
Should not have
• we don want it to be colorfull

```html
<!DOCTYPE html>
<html lang="tr">
<head>
<meta charset="utf-8">
<title>Vesk Mimarlık – Kartvizit</title>
<link rel="stylesheet" href="https://fonts.googleapis.com/css2?family=Open+Sans:wght@400;700&display=swap">
<style>
  :root{
    --stage:#1c1e20;
    --card:#ffffff;
    --band:#e6e6e6;
    --accent:#1f3f9e;
    --ink:#111111;
    --ghost:#e4e4e4;
  }
  *{margin:0;padding:0;box-sizing:border-box}
  html,body{width:1200px;height:720px;overflow:hidden;background:var(--stage)}
  body{position:relative;font-family:"Open Sans",Arial,sans-serif;color:var(--ink)}

  .card{position:absolute;background:var(--card);border-radius:12px;overflow:hidden}

  /* front */
  .card--front{left:92px;top:143px;width:538px;height:299px}
  .front__ghost{position:absolute;left:44px;top:36px;font-size:210px;font-weight:400;
    letter-spacing:-4px;color:var(--ghost);line-height:1;white-space:nowrap}
  .brand{position:absolute;font-weight:700;color:var(--ink);line-height:1}
  .brand__name{display:block;font-size:62px;letter-spacing:-1px}
  .brand__sub{display:block;font-size:17px;margin-top:6px;letter-spacing:.5px}
  .card--front .brand{left:200px;top:100px}

  /* back */
  .card--back{left:560px;top:250px;width:539px;height:298px}
  .back__art{position:absolute;inset:0}
  .card--back .brand{left:76px;top:103px}
  .holder{position:absolute;right:18px;top:42px;text-align:right;font-size:16.5px;line-height:24px}
  .contact{position:absolute;right:18px;top:182px;text-align:right;font-size:12px;line-height:17px}
  .contact__strong{font-weight:700}
</style>
</head>
<body>

<section class="card card--front" aria-label="Kartvizit ön yüz">
  <div class="front__ghost" aria-hidden="true">Vesk</div>
  <div class="brand">
    <span class="brand__name">Vesk</span>
    <span class="brand__sub">MİMARLIK</span>
  </div>
</section>

<section class="card card--back" aria-label="Kartvizit arka yüz">
  <svg class="back__art" width="539" height="298" viewBox="0 0 539 298" xmlns="http://www.w3.org/2000/svg">
    <defs>
      <linearGradient id="interiorTop" x1="0" y1="0" x2="1" y2="0">
        <stop offset="0" stop-color="#8fb0c8"/>
        <stop offset=".3" stop-color="#6a5a48"/>
        <stop offset=".65" stop-color="#3d3028"/>
        <stop offset="1" stop-color="#a8a49c"/>
      </linearGradient>
      <linearGradient id="interiorBottom" x1="0" y1="0" x2="1" y2="0">
        <stop offset="0" stop-color="#8a5a44"/>
        <stop offset=".3" stop-color="#2a2622"/>
        <stop offset=".6" stop-color="#7d7a74"/>
        <stop offset="1" stop-color="#b7aa98"/>
      </linearGradient>
    </defs>
    <rect x="0" y="0" width="539" height="18" fill="var(--band)"/>
    <polygon points="0,0 340,0 322,14 0,14" fill="var(--accent)"/>
    <polygon points="0,17 326,17 262,83 0,83" fill="url(#interiorTop)" role="img" aria-label="Otel ve restoran iç mekân fotoğrafları"/>
    <polygon points="0,215 256,215 318,281 0,281" fill="url(#interiorBottom)" role="img" aria-label="Bina cephesi, spa ve otel odası fotoğrafları"/>
    <rect x="0" y="281" width="539" height="17" fill="var(--band)"/>
    <polygon points="336,284 539,284 539,298 352,298" fill="var(--accent)"/>
  </svg>

  <div class="holder">
    <div>Deniz Arda KAYA - Mimar</div>
    <div>Architect</div>
  </div>

  <div class="brand">
    <span class="brand__name">Vesk</span>
    <span class="brand__sub">MİMARLIK</span>
  </div>

  <address class="contact" style="font-style:normal">
    <div>Selvi Mah. Rihtim Cad. Ayva Sok.</div>
    <div>No : 14 Merkez / ISTANBUL</div>
    <div class="contact__strong">t. 0216 555 01 40</div>
    <div class="contact__strong">f. 0216 555 01 41</div>
    <div>e.veskmimarlik@ornek-posta.com</div>
  </address>
</section>

</body>
</html>
```